Label Redesign For Hemp Oil Tincture Bottle*

I need a label redesigned for Marbleleaf Hemp, current bottle label and logo is attached. The current label doesn't standout, not sure if its the font size or colors on the existing label. It is very important to have on the label that this is a Premium Full Spectrum Hemp Oil that is 2000mg. Then after the label is redesigned and approved, I would need to packaging to be designed to match the approved label design.
This Hemp oil has a relaxing effect to help ease mental and emotional stress, tension and worry. The Omega Fatty Acids it contains also naturally improves your mood and overall brain function, causing you to feel more alert and focused. Hemp Oil helps with insomnia. Take some 2-3 hours before bedtime, you will feel relaxed yet aware of how tired you are that it will lead to a good night's sleep. Hemp Oil helps ease chronic pain and inflammation from conditions such as arthritis, fibromyalgia, lupus, and MS. As a pain relief supplement, it is a safer, natural, non-chemical and non-addictive alternative to prescription painkillers.

Target Market(s)

Adults

Industry/Entity Type

Supplement

Font styles to use
Serif
Sans Serif

Colors

Designer to choose colors to be used in the design.

Requirements
Must have
• All information thats on current label but where it says 750 in the front of the existing label, it needs to say 2000. The 2000 should be prominent on the label.

```html
<!DOCTYPE html>
<html lang="en">
<head>
<meta charset="utf-8">
<title>Marbleleaf Hemp – Full Spectrum Hemp Oil Label</title>
<link href="https://fonts.googleapis.com/css2?family=Open+Sans:wght@400;600;700&family=Tinos:wght@400;700&family=Great+Vibes&display=swap" rel="stylesheet">
<style>
  :root {
    --green: #5f9a3c;
    --green-dark: #3f7a2a;
    --green-band: rgba(70,125,45,.9);
    --green-light: #a6c98c;
    --script-tint: #eaf4dc;
    --ink: #222;
    --frame: #d6d6d6;
    --paper: #ffffff;
  }
  * { box-sizing: border-box; margin: 0; padding: 0; }
  html, body { width: 1200px; height: 621px; overflow: hidden; background: var(--paper); }
  body { font-family: "Open Sans", Arial, sans-serif; color: var(--ink); }
  .label {
    position: relative; width: 1200px; height: 621px;
    border: 3px solid var(--frame); overflow: hidden; background: var(--paper);
  }
  .brand {
    position: absolute; left: 16px; top: 20px;
    display: flex; align-items: center; gap: 10px;
    font-weight: 700; font-size: 22px; color: var(--green);
  }
  .brand-dot { width: 40px; height: 40px; border-radius: 50%; background: var(--green); }
  .zero-thc {
    position: absolute; left: 14px; top: 96px; width: 130px; height: 38px;
    background: var(--green); color: #fff; font-size: 22px; font-weight: 600;
    display: flex; align-items: center; justify-content: center;
  }
  .usage, .keep-out, .warnings {
    position: absolute; left: 14px; width: 330px; font-size: 13px; line-height: 1.55;
  }
  .usage { top: 150px; }
  .keep-out { top: 300px; font-weight: 700; }
  .warnings { top: 380px; }
  .heading { font-weight: 700; text-transform: uppercase; display: block; }

  .hero-art {
    position: absolute; left: 395px; top: 0; width: 410px; height: 430px;
    border-radius: 0 0 205px 205px;
    background: radial-gradient(circle at 60% 40%, #e9f2e2 0%, #bcd7a8 45%, #6f9e55 100%);
  }
  .title-band {
    position: absolute; left: 395px; top: 150px; width: 410px; height: 175px;
    background: var(--green-band); color: #fff; text-align: center;
    font-family: "Tinos", "Times New Roman", serif;
    display: flex; flex-direction: column; justify-content: center; align-items: center;
  }
  .title-band .premium { font-family: "Great Vibes", cursive; color: var(--script-tint); font-size: 30px; line-height: 32px; }
  .title-band .main { font-size: 36px; line-height: 40px; }
  .title-band .strength {
    font-family: "Tinos", "Times New Roman", serif; font-weight: 700;
    font-size: 52px; line-height: 54px; color: var(--script-tint); letter-spacing: 2px;
  }
  .title-band .strength small { font-size: 26px; font-weight: 400; letter-spacing: 0; }

  .product-specs {
    position: absolute; left: 380px; top: 445px; width: 440px; text-align: center;
    font-family: "Tinos", "Times New Roman", serif; font-size: 32px; line-height: 40px;
  }

  .facts {
    position: absolute; left: 850px; top: 170px; width: 290px; height: 255px;
    background: var(--green-light); font-size: 13px; border: 2px solid var(--green-dark);
  }
  .facts .row { padding: 7px 10px; border-bottom: 2px solid var(--green-dark); display: flex; justify-content: space-between; }
  .facts .title { display: block; padding: 8px 10px; border-bottom: 2px solid var(--green-dark); line-height: 1.5; }
  .facts .title strong { font-weight: 700; }
  .facts .other { padding: 8px 10px; line-height: 1.5; }

  .distributor {
    position: absolute; left: 850px; top: 495px; width: 290px; padding: 8px 10px;
    background: var(--green-light); font-size: 13px; line-height: 1.45;
  }
  .batch {
    position: absolute; left: 1155px; top: 20px; height: 580px; width: 30px;
    writing-mode: vertical-rl; color: var(--green-light); font-size: 14px;
    display: flex; justify-content: space-around;
  }
</style>
</head>
<body>
<div class="label">
  <div class="brand"><span class="brand-dot"></span>Marbleleaf Hemp</div>
  <div class="zero-thc">Zero THC</div>

  <p class="usage"><span class="heading">Suggested Use :</span>Shake well before each use. Take 30 drops (1 full dropper) and place in mouth underneath tongue for 30 seconds 1-2 times daily or as recommended by a Physician.</p>
  <p class="keep-out">KEEP OUT OF REACH OF CHILDREN<br>DO NOT USE IF SEAL IS BROKEN OR MISSING</p>
  <p class="warnings"><strong>WARNINGS:</strong> If you are pregnant or breastfeeding, consult a health care practitioner before using.</p>

  <div class="hero-art" role="img" aria-label="Photograph of a green hemp plant against a soft light background"></div>
  <div class="title-band">
    <span class="premium">Premium</span>
    <span class="main">Full Spectrum</span>
    <span class="strength">2000 <small>mg</small></span>
    <span class="main">Hemp Oil</span>
  </div>

  <div class="product-specs">
    <p>2000 mg</p>
    <p>Dietary Supplement</p>
    <p>1 fl oz (30ml)</p>
    <p>Natural Peppermint flavor</p>
  </div>

  <div class="facts">
    <span class="title"><strong>Supplement Facts</strong><br>Serving Size 1ml<br>Serving Per Container 30</span>
    <div class="row"><span>Calories 8</span><span>Calories Fat 8</span></div>
    <div class="row"><span>Total Fat</span><span>1g 2%</span></div>
    <div class="row"><span>Full Spectrum Hemp Extract</span><span>1g 2%</span></div>
    <p class="other">Other Ingredients: Hemp seed oil, Grape Seed oil, Peppermint and Stevia</p>
  </div>

  <div class="distributor">
    <strong>DISTRIBUTED FOR:</strong><br>
    Greenvale Extracts, INC.<br>
    support@marbleleafhemp.com
  </div>

  <div class="batch"><span>Lot No. 00000</span><span>Best By 00/00</span></div>
</div>
</body>
</html>
```